Business Card Design

New business card design

Target Market(s)

Residential & Commercial Property Managers

Industry/Entity Type

Plumbing Services

Contact Information for Business Card

Name - Owen Tredgold, title - Director, Phone Number - 0431 862 507, email - owen@rvb-plumbing.com.au, Company ABN - 73 215 904 386,

Font styles to use
Sans Serif

Colors
0054AA
0677BA
7BADD7
CADEEF
E8F1F8

```html
<!DOCTYPE html>
<html lang="en">
<head>
<meta charset="utf-8">
<title>RVB Plumbing Services – Business Card</title>
<link href="https://fonts.googleapis.com/css2?family=Roboto:wght@300;400;700&display=swap" rel="stylesheet">
<style>
  :root {
    --bg: #3a3a3c;
    --card: #1d1d1f;
    --card-panel: #2a2a2c;
    --blue: #1ea0e6;
    --taupe: #8a8177;
    --black: #111112;
    --white: #ffffff;
    --grey-text: #6e6e70;
    --pattern-dark: #151517;
    --pattern-light: #4a4a4c;
  }
  * { box-sizing: border-box; margin: 0; padding: 0; }
  html, body {
    width: 1200px; height: 852px; overflow: hidden;
    background: var(--bg);
    font-family: "Roboto", Arial, sans-serif;
  }
  .stage { position: relative; width: 1200px; height: 852px; }
  .card {
    position: absolute; width: 500px; height: 290px;
    border-radius: 22px; overflow: hidden;
    background: var(--card);
    box-shadow: 0 10px 30px rgba(0,0,0,.45);
  }
  .card--back { left: 70px; top: 150px; }
  .card--front { left: 630px; top: 412px; }

  .back-pattern {
    position: absolute; inset: 0;
    background: linear-gradient(135deg, var(--pattern-dark) 0%, #2c2c2e 55%, var(--pattern-light) 100%);
  }

  .front-waves { position: absolute; inset: 0; width: 500px; height: 290px; }

  .brand {
    position: absolute; left: 28px; top: 140px;
    display: flex; align-items: center; gap: 9px;
  }
  .brand-dot { width: 13px; height: 13px; border-radius: 50%; background: var(--blue); }
  .brand-name {
    color: var(--white); font-weight: 300; font-size: 20px; letter-spacing: .3px;
    line-height: 1.1; white-space: nowrap;
  }

  .person { position: absolute; right: 22px; top: 16px; text-align: right; }
  .person-name { color: var(--white); font-weight: 700; font-size: 16px; line-height: 20px; }
  .person-title { color: var(--grey-text); font-weight: 400; font-size: 10.5px; line-height: 14px; }

  .contact {
    position: absolute; right: 18px; top: 84px;
    list-style: none; text-align: right;
  }
  .contact-item {
    display: flex; justify-content: flex-end; align-items: center; gap: 7px;
    color: var(--white); font-size: 10.5px; font-weight: 300; line-height: 18px;
    white-space: nowrap;
  }
  .contact-icon { width: 10px; height: 10px; fill: var(--blue); flex: none; }
</style>
</head>
<body>
<main class="stage">
  <section class="card card--back">
    <div class="back-pattern" role="img" aria-label="Embossed water-droplet pattern with one blue droplet"></div>
  </section>

  <section class="card card--front">
    <svg class="front-waves" viewBox="0 0 500 290" aria-hidden="true">
      <path class="wave-panel" d="M500,62 C400,64 320,80 290,140 C265,190 240,255 140,284 L140,290 L500,290 Z" fill="var(--card-panel)"/>
      <path class="wave-taupe" d="M296,168 C276,220 246,266 160,290 L206,290 C266,266 290,222 303,180 Z" fill="var(--taupe)"/>
      <path class="wave-black" d="M305,192 C292,236 268,270 222,290 L500,290 L500,258 C410,258 340,236 305,192 Z" fill="var(--black)"/>
      <path class="wave-line" d="M500,62 C400,64 320,80 290,140 C265,190 240,255 140,284" fill="none" stroke="var(--blue)" stroke-width="4"/>
    </svg>

    <div class="brand">
      <span class="brand-dot"></span>
      <span class="brand-name">RVB Plumbing Services</span>
    </div>

    <div class="person">
      <p class="person-name">Owen Tredgold</p>
      <p class="person-title">Director</p>
    </div>

    <ul class="contact">
      <li class="contact-item">0431 862 507
        <svg class="contact-icon" viewBox="0 0 24 24"><path d="M6.6 10.8a15.1 15.1 0 0 0 6.6 6.6l2.2-2.2c.3-.3.7-.4 1-.2 1.1.4 2.3.6 3.6.6.6 0 1 .4 1 1V20c0 .6-.4 1-1 1A17 17 0 0 1 3 4c0-.6.4-1 1-1h3.5c.6 0 1 .4 1 1 0 1.3.2 2.5.6 3.6.1.3 0 .7-.2 1z"/></svg>
      </li>
      <li class="contact-item">owen@rvb-plumbing.com.au
        <svg class="contact-icon" viewBox="0 0 24 24"><path d="M2 5h20v14H2z M2 5l10 8 10-8" fill="var(--blue)" stroke="var(--card-panel)" stroke-width="1.5"/></svg>
      </li>
      <li class="contact-item">www.rvb-plumbing.com.au
        <svg class="contact-icon" viewBox="0 0 24 24"><circle cx="12" cy="12" r="10"/><path d="M2 12h20M12 2c3 3 3 17 0 20M12 2c-3 3-3 17 0 20" fill="none" stroke="var(--card-panel)" stroke-width="1.5"/></svg>
      </li>
      <li class="contact-item">12 Harbour Rd, Brookvale NSW 2100
        <svg class="contact-icon" viewBox="0 0 24 24"><path d="M12 2a7 7 0 0 0-7 7c0 5 7 13 7 13s7-8 7-13a7 7 0 0 0-7-7zm0 9.5a2.5 2.5 0 1 1 0-5 2.5 2.5 0 0 1 0 5z"/></svg>
      </li>
    </ul>
  </section>
</main>
</body>
</html>
```